Vel-Trax.ch is looking for business card letterhead and envelope C5 with WOW effect

We need a strong business card for our company Vel-Trax.ch, logo is available. You want a black or dark background on which the logo Stark r% 26 # 252; appears. Letterhead and envelope in C5 format should be in a similar design, but does not have to be We need a strong business card for our company Vel-Trax.ch, logo is available. A black or dark background is desired, on which the logo Stark comes across. The letterhead and the envelope in C5 format should have a similar design.

Target Market(s)

Private customers as well as entrepreneurs

Contact Information for Business Card

E-mail: info@vel-trax.ch
Web.www.Vel-Trax.ch
Tel: +41 ( 0 ) 79 684 3027
Adresse:
Lindenhaldeweg 14
9403 Brenzikon

Hier kann man Icons verwenden für Email,Tel und Adressse

Font styles to use
Other font styles liked:
• Dubai,bold

Colors

Designer to choose colors to be used in the design.

Requirements
Must have
• WOW effect
Nice to have
• R% 26 # 252; back business card with our service listings. - VEHICLE LABELING - SHOP WINDOW LABELING - STICKERS AND MUCH MORE ... in red color

```html
<!DOCTYPE html>
<html lang="en">
<head>
<meta charset="utf-8">
<title>Vel-Trax.ch – Business Card</title>
<link rel="stylesheet" href="https://fonts.googleapis.com/css2?family=Russo+One&family=Open+Sans:wght@400;600;700&display=swap">
<style>
  :root {
    --canvas: #e6e3df;
    --card: #231f20;
    --yellow: #f2c314;
    --white: #ffffff;
    --ink: #231f20;
  }
  * { box-sizing: border-box; margin: 0; padding: 0; }
  html, body { width: 1200px; height: 843px; overflow: hidden; }
  body {
    background: var(--canvas);
    display: flex;
    align-items: center;
    justify-content: center;
    gap: 40px;
    font-family: "Open Sans", sans-serif;
  }
  .card {
    position: relative;
    width: 540px;
    height: 310px;
    background: var(--card);
    overflow: hidden;
    box-shadow: 0 6px 18px rgba(0,0,0,.18);
  }

  /* Front: logo side */
  .brand {
    position: absolute;
    top: 52px;
    left: 150px;
    display: flex;
    align-items: center;
    gap: 16px;
  }
  .brand-mark {
    width: 70px;
    height: 70px;
    background: var(--yellow);
  }
  .brand-name {
    font-family: "Russo One", sans-serif;
    font-size: 31px;
    color: var(--white);
    letter-spacing: 1px;
  }
  .services {
    position: absolute;
    right: 38px;
    top: 168px;
    list-style: none;
    font-size: 10px;
    font-weight: 600;
    line-height: 1.25;
    color: var(--white);
    text-transform: uppercase;
  }
  .services li::before { content: "• "; }
  .card-graphics { position: absolute; inset: 0; }
  .contact {
    position: absolute;
    left: 42px;
    top: 226px;
    font-size: 12px;
    color: var(--white);
    line-height: 1.45;
  }
  .contact-row { display: flex; align-items: center; gap: 9px; }
  .contact-row svg { width: 12px; height: 12px; flex: none; }
  .web-strip {
    position: absolute;
    left: 48px;
    top: 286px;
    height: 18px;
    line-height: 18px;
    font-size: 11px;
    font-weight: 700;
    letter-spacing: 4px;
    color: var(--ink);
    white-space: nowrap;
  }

  /* Back: pattern side */
  .pattern-area {
    position: absolute;
    left: 0;
    bottom: 0;
    width: 350px;
    height: 250px;
    background: var(--yellow);
    clip-path: polygon(0 0, 45% 0, 60% 30%, 100% 60%, 92% 100%, 0 100%);
  }
  .back-title {
    position: absolute;
    right: 32px;
    top: 40px;
    text-align: right;
    color: var(--yellow);
  }
  .back-name {
    font-family: "Russo One", sans-serif;
    font-size: 36px;
    letter-spacing: 1px;
    line-height: 1;
  }
  .back-web {
    font-size: 13px;
    font-weight: 700;
    letter-spacing: 5px;
    margin-top: 4px;
  }
</style>
</head>
<body>

  <section class="card card-front">
    <svg class="card-graphics" viewBox="0 0 540 310" aria-hidden="true">
      <line x1="40" y1="218" x2="500" y2="218" stroke="var(--yellow)" stroke-width="1.2"/>
      <polygon points="318,286 338,262 540,262 540,304 302,304" fill="var(--yellow)"/>
      <polygon points="30,286 318,286 302,304 30,304" fill="var(--white)"/>
      <rect x="0" y="304" width="540" height="6" fill="var(--yellow)"/>
    </svg>

    <div class="brand">
      <span class="brand-mark"></span>
      <span class="brand-name">VEL-TRAX.CH</span>
    </div>

    <ul class="services">
      <li>Vehicle labeling</li>
      <li>Shop window labeling</li>
      <li>Stickers and much more</li>
    </ul>

    <div class="contact">
      <div class="contact-row">
        <svg viewBox="0 0 24 24"><path d="M6.6 10.8a15 15 0 0 0 6.6 6.6l2.2-2.2a1 1 0 0 1 1-.25 11.4 11.4 0 0 0 3.6.6 1 1 0 0 1 1 1V20a1 1 0 0 1-1 1A17 17 0 0 1 3 4a1 1 0 0 1 1-1h3.5a1 1 0 0 1 1 1c0 1.25.2 2.45.6 3.6a1 1 0 0 1-.25 1z" fill="none" stroke="var(--yellow)" stroke-width="2"/></svg>
        <span>+41 ( 0 ) 79 684 3027</span>
      </div>
      <div class="contact-row">
        <svg viewBox="0 0 24 24"><rect x="2" y="5" width="20" height="14" fill="none" stroke="var(--yellow)" stroke-width="2"/><path d="M2 5l10 8 10-8" fill="none" stroke="var(--yellow)" stroke-width="2"/></svg>
        <span>info@vel-trax.ch</span>
      </div>
    </div>

    <div class="web-strip">www.Vel-Trax.ch</div>
  </section>

  <section class="card card-back">
    <div class="pattern-area" role="img" aria-label="Yellow honeycomb hexagon pattern"></div>
    <div class="back-title">
      <div class="back-name">VEL-TRAX.CH</div>
      <div class="back-web">www.Vel-Trax.ch</div>
    </div>
  </section>

</body>
</html>
```